Design of a promotional offer flyer required to promote low-cost websites to 1-man band businesses

I want a flyer designed - either a double-sided A5 flyer or even A4 folded into a third double-sided. The flyer is to showcase a new service - low-cost websites for 1-man-band businesses, business startups and tradesmen in England. Look at the copy, find some pix and let me know! Flyer will be printed and used as an image on my website too. Pix could be related to some of the target groups. We need to stress the simple message that websites start from £5 per week and this is an-all-in-one fee.

Target Market(s)

Tradesmen, business start ups and 1-man band businesses that want a website

Industry/Entity Type

Small Business

Contact Information for Business Card

All contact details and name of business to be confirmed shortly

Font styles to use
Serif

Requirements
Must have
• Basic messages from copy for flyer i.e. websites from £5 per week and what each client gets for that price to be included on the business card! Please read copy for the flyer.
Nice to have
• Nice background image or series of small images relevant to the target audience. Again, see list of targets from copy for flyer.
Should not have
• I don't want exact or similar design to my main business Blue Harbour Promotions. The new flyer and business card should be a different and distinct branding to that of Blue Harbour Promotions. Aimed at a more economical style, whilst looking professional, but relevant to the target audiences.

```html
<!DOCTYPE html>
<html lang="en">
<head>
<meta charset="utf-8">
<title>Low-Cost Website Flyer</title>
<link rel="stylesheet" href="https://fonts.googleapis.com/css2?family=Oswald:wght@500;600;700&family=Lato:wght@400;700&family=Roboto+Condensed:wght@700&display=swap">
<style>
  :root {
    --brand-red: #d7072a;
    --ink: #111111;
    --panel-grey: #e6e6e6;
    --paper: #ffffff;
    --stage: #f3f3f3;
    --body-text: #1c1c1c;
  }
  * { margin: 0; padding: 0; box-sizing: border-box; }
  html, body { width: 1200px; height: 1200px; overflow: hidden; background: var(--stage); }
  .canvas { position: relative; width: 1200px; height: 1200px; }

  .page { position: absolute; top: 204px; width: 560px; height: 792px; overflow: hidden; background: var(--paper); box-shadow: 0 4px 18px rgba(0,0,0,.18); }
  .page--back { left: 40px; }
  .page--cover { left: 600px; }
  .page-art { position: absolute; inset: 0; width: 560px; height: 792px; }

  /* Back page */
  .about { position: absolute; left: 43px; top: 60px; width: 478px; color: var(--body-text); }
  .about__title { font-family: "Oswald", sans-serif; font-weight: 600; font-size: 18px; line-height: 24px; color: var(--brand-red); letter-spacing: .3px; margin-bottom: 2px; }
  .about__text { font-family: "Lato", sans-serif; font-size: 12.3px; line-height: 15.6px; margin-bottom: 10px; }
  .about__text--narrow { width: 455px; }

  .offer-badge { position: absolute; left: 206px; top: 377px; width: 258px; height: 258px; border-radius: 50%; background: var(--brand-red); border: 4px solid var(--ink); display: flex; flex-direction: column; align-items: center; justify-content: center; text-align: center; color: var(--paper); font-family: "Oswald", sans-serif; font-weight: 600; font-size: 19px; line-height: 28px; text-transform: uppercase; padding-top: 4px; white-space: nowrap; }
  .offer-badge__price { font-size: 29px; }

  .contact { position: absolute; right: 32px; top: 668px; text-align: right; color: var(--paper); }
  .contact__name { font-family: "Oswald", sans-serif; font-weight: 600; font-size: 25px; line-height: 30px; margin-bottom: 6px; }
  .contact__line { font-family: "Lato", sans-serif; font-size: 12.5px; line-height: 22.5px; }

  /* Cover */
  .cover-name { position: absolute; left: 40px; top: 40px; font-family: "Oswald", sans-serif; font-weight: 700; font-size: 50px; line-height: 60px; color: var(--paper); letter-spacing: .5px; }
  .headline { position: absolute; right: 40px; top: 626px; text-align: right; }
  .headline__main { font-family: "Oswald", sans-serif; font-weight: 700; font-size: 47px; line-height: 54px; color: var(--brand-red); text-transform: uppercase; }
  .headline__sub { font-family: "Roboto Condensed", sans-serif; font-weight: 700; font-size: 32px; line-height: 36px; color: var(--ink); }
  .headline__email { font-family: "Lato", sans-serif; font-size: 12.5px; letter-spacing: 4px; color: var(--ink); margin-top: 14px; }
</style>
</head>
<body>
<div class="canvas">

  <section class="page page--back">
    <svg class="page-art" viewBox="0 0 560 792" xmlns="http://www.w3.org/2000/svg">
      <defs>
        <linearGradient id="glow" x1="0" y1="0" x2="0" y2="1">
          <stop offset="0" stop-color="#ffffff"/>
          <stop offset=".55" stop-color="#d2d2d2"/>
          <stop offset="1" stop-color="#5e5e5e"/>
        </linearGradient>
        <linearGradient id="dark" x1="0" y1="0" x2="0" y2="1">
          <stop offset="0" stop-color="#2c2c2c"/>
          <stop offset=".6" stop-color="#111"/>
          <stop offset="1" stop-color="#000"/>
        </linearGradient>
      </defs>
      <rect width="560" height="792" fill="var(--panel-grey)"/>
      <polygon points="0,283 331,500 126,792 0,792" fill="url(#glow)" role="img" aria-label="Smartphone glowing with a network of message icons over a world map"/>
      <polygon points="560,173 560,792 126,792" fill="url(#dark)" role="img" aria-label="Dim photo of a businessman in a suit surrounded by app icons"/>
    </svg>

    <div class="about">
      <h2 class="about__title">ABOUT US</h2>
      <p class="about__text">Lorem Ipsum is simply dummy text of the printing and typesetting industry. Lorem Ipsum has been the industry's standard dummy text ever since the 1500s, when an unknown printer took a galley of type and scrambled it to make a type specimen book. It has survived not only five centuries, but also the leap into electronic typesetting, remaining essentially unchanged. It was popularised in the 1960s with the release of Lettersheet sheets containing Lorem Ipsum passages, and more recently with desktop publishing software like Pagesmith Studio including versions of Lorem Ipsum.</p>
      <p class="about__text about__text--narrow">Lorem Ipsum is simply dummy text of the printing and typesetting industry. Lorem Ipsum has been the industry's standard dummy text ever since the 1500s, when an unknown printer took a galley of type and scrambled it to make a type specimen book. It has survived not only five centuries, but also the leap into electronic typesetting, remaining essentially unchanged.</p>
    </div>

    <div class="offer-badge">
      <span>For an-all-in fee from</span>
      <span>Only <span class="offer-badge__price">£5</span> per week</span>
      <span>For a 1-page website or</span>
      <span><span class="offer-badge__price">£10</span> per week for a</span>
      <span>5-page website.</span>
    </div>

    <div class="contact">
      <p class="contact__name">COMPANY LOGO</p>
      <p class="contact__line">info@yourcompany.co.uk</p>
      <p class="contact__line">sales@yourcompany.co.uk</p>
      <p class="contact__line">yourname@yourcompany.co.uk</p>
    </div>
  </section>

  <section class="page page--cover">
    <svg class="page-art" viewBox="0 0 560 792" xmlns="http://www.w3.org/2000/svg">
      <defs>
        <linearGradient id="hero" x1="0" y1="0" x2="1" y2="1">
          <stop offset="0" stop-color="#8fa6c4"/>
          <stop offset=".45" stop-color="#2a2f38"/>
          <stop offset="1" stop-color="#7d8ea8"/>
        </linearGradient>
      </defs>
      <rect width="560" height="792" fill="var(--paper)"/>
      <rect x="0" y="175" width="548" height="425" fill="url(#hero)" role="img" aria-label="Businessman holding out a laptop, tablet and phone linked by a glowing network"/>
      <polygon points="0,0 477,0 363,175 0,175" fill="var(--brand-red)"/>
      <polygon points="0,175 363,175 86,600 0,600" fill="var(--brand-red)" opacity=".82"/>
      <polygon points="0,600 86,600 0,732" fill="var(--brand-red)"/>
    </svg>

    <p class="cover-name">COMPANY LOGO</p>

    <div class="headline">
      <h1 class="headline__main">Want a Website</h1>
      <p class="headline__sub">Without It Costing The Earth?</p>
      <p class="headline__email">yourname@yourcompany.co.uk</p>
    </div>
  </section>

</div>
</body>
</html>
```